Strategy and Technology Consulting - Our Story and Values Page

Interior Page design – Our History and Our Values

Our homepage has been designed and we are looking for a design for one of the interior pages. This interior page tells the story of Our History and Our Values

Because the homepage has been designed, we would like this interior page to reflect the design of the homepage without being a mirror image of the homepage.

This site will be implemented in WordPress using the Elementor framework.

Font: Poppins medium and Poppins dark
Illustrations: Our homepage illustrations were designed by “Teslo 1964” on Imagevale. Compatible original or stock illustrations are welcome. Stock photography is also welcome. Teslo is also available through Teslo Bramen on Portvue

• Homepage design – this is the design we will use for our homepage. Contest entries should reflect this basic style but should be distinctly different from the homepage.
• Our History and Our Values – Wireframe – the basic layout of the page we are looking for.
• Our History and Our Values – Word document with the text supporting the wireframe.
• Color Palette – please use colors compatible with the palette attached.

Our Story - timeline
There is a timeline element in the wireframe. The wireframe displays this as a series of chevrons (arrows), but it does not need to be. Creativity in display of the timeline is appreciated.

Our Values
If you look at the Word document, you will see that there are a lot of words on the page. The winning design will present the information in a way that engages the user without overwhelming them with too much to read. For example, they may click on a value and see more information.

Target Market(s)

CIO's and Technology Executives

Number of Pages Required

1 page

Font styles to use
Sans Serif
Other font styles liked:
• Poppin

Requirements
Must have
• A timeline element, all of our values
Nice to have
• Clever timeline display

```html
<!DOCTYPE html>
<html lang="en">
<head>
<meta charset="utf-8">
<title>Our Story &amp; Values – Veltrax</title>
<link href="https://fonts.googleapis.com/css2?family=Poppins:wght@400;500;600;700&display=swap" rel="stylesheet">
<style>
:root{
  --ink:#3b4556;
  --text:#4f5868;
  --slate:#465469;
  --slate-dark:#3a4557;
  --footer:#4b5a73;
  --bar:#3f4b5f;
  --gold:#f0b323;
  --blue:#3f5ca9;
  --blue-soft:#e6ebf7;
  --card:#ffffff;
  --page:#f7f7f9;
}
*{margin:0;padding:0;box-sizing:border-box}
html,body{width:1200px;height:4006px;overflow:hidden}
body{font-family:"Poppins",sans-serif;color:var(--text);background:#fff;position:relative}
.abs{position:absolute}

/* header */
.site-header{position:absolute;left:0;top:0;width:1200px;height:95px}
.brand{position:absolute;left:93px;top:22px;display:flex;align-items:center;gap:10px;font-size:44px;font-weight:400;color:#8d96a3;letter-spacing:1px}
.brand-dot{width:14px;height:14px;border-radius:50%;background:var(--blue)}
.nav{position:absolute;left:542px;top:36px;display:flex;gap:24px;align-items:center;font-size:12px;font-weight:600;color:var(--ink)}
.nav .home{width:14px;height:13px}
.nav span::after{content:" ⌄";font-size:10px}
.btn{background:var(--gold);color:#fff;font-weight:600;font-size:12px;border-radius:22px;display:inline-flex;align-items:center;justify-content:center}
.header-btn{position:absolute;left:979px;top:27px;width:133px;height:38px}

/* story */
.story-bg{position:absolute;left:0;top:95px;width:1200px;height:700px;background:linear-gradient(180deg,#fff 0%,#f4f4f6 45%,#fff 100%)}
.section-title{position:absolute;left:0;width:1200px;text-align:center;font-size:31px;font-weight:600;color:var(--ink)}
.tl-card{position:absolute;top:190px;width:300px;height:281px;background:var(--card);box-shadow:0 6px 24px rgba(60,70,90,.08)}
.tl-tag{position:absolute;left:-16px;top:23px;height:36px;padding:0 44px 0 36px;background:var(--slate);color:#fff;font-weight:600;font-size:19px;line-height:36px;clip-path:polygon(0 0,100% 0,90% 100%,0 100%)}
.tl-list{position:absolute;left:18px;top:80px;right:18px;list-style:none;font-size:15.5px;line-height:20px;color:var(--ink)}
.tl-list li{position:relative;padding-left:18px;margin-bottom:10px}
.tl-list li::before{content:"";position:absolute;left:0;top:6px;width:9px;height:9px;border-radius:50%;border:2.5px solid var(--gold)}
.tl-list li.sub{padding-left:14px;margin-bottom:6px}
.tl-list li.sub::before{border:none;background:var(--ink);width:4px;height:4px;top:9px}
.tl-link{position:absolute;top:324px}

/* values */
.values-sub{position:absolute;left:0;top:610px;width:1200px;text-align:center;font-size:21px;font-weight:500;color:var(--ink)}
.values-intro{position:absolute;left:190px;top:648px;width:820px;text-align:center;font-size:16px;line-height:28px}
.value-title{position:absolute;font-size:28px;font-weight:600;color:var(--ink)}
.value-text{position:absolute;width:480px;font-size:16px;line-height:27.5px}
.art{position:absolute;border-radius:50%;background:radial-gradient(circle at 50% 45%,#dfe6f6 0%,#e9edf8 60%,#f3f5fb 100%)}

/* newsletter + footer */
.footer-wave{position:absolute;left:0;top:3280px;width:1200px;height:726px}
.newsletter{position:absolute;left:137px;top:3291px;width:924px;height:206px;border-radius:103px;background:var(--gold)}
.nl-title{position:absolute;left:81px;top:54px;font-size:32px;font-weight:700;color:#fff}
.nl-text{position:absolute;left:81px;top:110px;font-size:15px;line-height:19px;font-weight:500;color:#fff}
.nl-field{position:absolute;left:549px;top:79px;width:320px;height:48px;border-radius:24px;background:#fff;display:flex;align-items:center;padding-left:22px;font-size:12px;color:#8a93a2;gap:10px}
.nl-send{position:absolute;right:4px;top:4px;width:40px;height:40px;border-radius:50%;background:#9aa4b4;display:flex;align-items:center;justify-content:center}

.f-brand{position:absolute;left:118px;top:3682px;display:flex;align-items:center;gap:12px;font-size:60px;color:#d9dde4;letter-spacing:1px}
.f-brand .brand-dot{width:18px;height:18px;background:var(--gold)}
.socials{position:absolute;left:176px;top:3762px;display:flex;gap:13px}
.socials span{width:38px;height:38px;border-radius:50%;background:#6b7890}
.footer-btn{position:absolute;left:214px;top:3824px;width:132px;height:36px}
.f-col{position:absolute;top:3656px;color:#fff}
.f-col h4{font-size:19px;font-weight:600;margin-bottom:14px}
.f-col ul{list-style:none;font-size:12px;line-height:31px}
.f-col li::before{content:"›";margin-right:8px}
.contact-item{position:relative;padding-left:24px;font-size:12px;line-height:17px;margin-bottom:18px;width:190px}
.contact-item svg{position:absolute;left:0;top:2px}
.copyright{position:absolute;left:0;top:3940px;width:1200px;height:66px;background:var(--bar);color:#fff;text-align:center;font-size:13px;line-height:66px}
.chat{position:absolute;left:1136px;top:3908px;width:46px;height:46px;border-radius:50%;background:var(--gold);display:flex;align-items:center;justify-content:center}
</style>
</head>
<body>

<header class="site-header">
  <div class="brand"><span class="brand-dot"></span>Veltrax</div>
  <nav class="nav">
    <svg class="home" viewBox="0 0 14 13"><path d="M7 0 0 6h2v7h4V9h2v4h4V6h2z" fill="#8d96a3"/></svg>
    <span>ABOUT US</span><span>SERVICES</span><span>INSIGHTS</span><span>JOIN US</span>
  </nav>
  <a class="btn header-btn">CONTACT US</a>
</header>

<div class="story-bg"></div>
<h1 class="section-title" style="top:116px">Our Story</h1>

<div class="tl-card" style="left:92px">
  <div class="tl-tag">2017 – 2019</div>
  <ul class="tl-list">
    <li>Growth Strategy Focus</li>
    <li>Consistent, Modest Growth</li>
    <li>Preliminary Focus on Technology</li>
    <li><b>Eureka!</b> Implementing strategy is hard .</li>
  </ul>
</div>
<div class="tl-card" style="left:449px">
  <div class="tl-tag">2020 – 2021</div>
  <ul class="tl-list">
    <li>Pandemic Pauses Growth</li>
    <li><b>Rethinking :</b></li>
    <li class="sub">The Business Model</li>
    <li class="sub">The Delivery Model</li>
  </ul>
</div>
<div class="tl-card" style="left:814px">
  <div class="tl-tag">2022 &amp; Onward</div>
  <ul class="tl-list">
    <li>Leadership Team for Focus on Essential Areas</li>
    <li>Rapid Growth</li>
    <li>Customer Success</li>
  </ul>
</div>
<svg class="tl-link" style="left:382px" width="78" height="16"><circle cx="8" cy="8" r="6.5" fill="#fff" stroke="#6d7687" stroke-width="1.5"/><circle cx="70" cy="8" r="6.5" fill="#fff" stroke="#6d7687" stroke-width="1.5"/><line x1="15" y1="8" x2="63" y2="8" stroke="#6d7687" stroke-dasharray="2 2"/></svg>
<svg class="tl-link" style="left:741px" width="78" height="16"><circle cx="8" cy="8" r="6.5" fill="#fff" stroke="#6d7687" stroke-width="1.5"/><circle cx="70" cy="8" r="6.5" fill="#fff" stroke="#6d7687" stroke-width="1.5"/><line x1="15" y1="8" x2="63" y2="8" stroke="#6d7687" stroke-dasharray="2 2"/></svg>

<h2 class="section-title" style="top:563px">Our Values</h2>
<p class="values-sub">The Value of Every Human.Regardless.</p>
<p class="values-intro">Each person's unique experiences and perspectives add vibrant hues to the tapestry of our shared existence.&nbsp; In a world where diversity paints the canvas of humanity, true beauty is found in recognizing the inherent and incalculable value of every human being.</p>

<!-- Collaboration -->
<div class="art" role="img" aria-label="Illustration of two colleagues shaking hands among puzzle pieces and growth charts" style="left:93px;top:795px;width:428px;height:388px"></div>
<h3 class="value-title" style="left:633px;top:878px">Collaboration</h3>
<p class="value-text" style="left:633px;top:926px">Collaboration in work transforms individual endeavors into symphonies of collective achievement. Through collaboration, diverse talents converge, fostering a rich exchange of ideas that amplifies creativity, accelerates progress, and brings forth solutions beyond what a single mind could conceive.</p>

<!-- Passion -->
<h3 class="value-title" style="left:93px;top:1308px">Passion</h3>
<p class="value-text" style="left:93px;top:1357px;width:500px">Passion infuses our work with energy, transforming routine tasks into opportunities for creativity and innovation. Fueled by passion, individuals become unstoppable forces, driven to overcome challenges and achieve remarkable outcomes that benefit them and inspire those around them</p>
<div class="art" role="img" aria-label="Illustration of a person climbing with a flag against a city skyline and rising arrows" style="left:660px;top:1215px;width:428px;height:370px"></div>

<!-- Excellence -->
<div class="art" role="img" aria-label="Illustration of people working on laptops around a stopwatch, target and circular arrows" style="left:90px;top:1593px;width:470px;height:373px"></div>
<h3 class="value-title" style="left:633px;top:1688px">Excellence</h3>
<p class="value-text" style="left:633px;top:1737px">Excellence isn't a destination; it's a continuous journey of refinement and growth. Striving for excellence cultivates a culture of continuous improvement, fostering innovation, credibility, and a lasting impact that resonates far beyond the immediate task.</p>

<!-- Tenacity -->
<h3 class="value-title" style="left:93px;top:2074px">Tenacity</h3>
<p class="value-text" style="left:93px;top:2123px;width:500px">Tenacity is the unwavering anchor that keeps us grounded amidst adversity, propelling us forward when faced with obstacles. The resilience to persist, adapt, and learn from setbacks leads to the mastery of skills and the fulfillment of ambitious goals.</p>
<div class="art" role="img" aria-label="Illustration of a person celebrating with a flag on a mountain peak" style="left:663px;top:1975px;width:428px;height:380px"></div>

<!-- Solution Mindset -->
<div class="art" role="img" aria-label="Illustration of a person fitting a large puzzle piece among gears" style="left:93px;top:2370px;width:430px;height:396px"></div>
<h3 class="value-title" style="left:633px;top:2482px">Solution Mindset</h3>
<p class="value-text" style="left:633px;top:2531px">A solution mindset is the compass that directs our focus from problems to possibilities. It empowers us to navigate challenges with a proactive mindset, igniting a journey of exploration and innovation that not only resolves issues but also paves the way for continuous growth &amp; success.</p>

<!-- Generosity -->
<h3 class="value-title" style="left:93px;top:2900px">Generosity</h3>
<p class="value-text" style="left:93px;top:2949px;width:500px">Generosity creates a virtuous cycle of goodwill, fostering a sense of unity and shared purpose among colleagues. By freely sharing knowledge, support, and resources, we uplift those around us and contribute to a collaborative environment where collective achievements flourish.</p>
<div class="art" role="img" aria-label="Illustration of two businessmen shaking hands with coins and plants around them" style="left:660px;top:2790px;width:428px;height:396px"></div>

<!-- footer background -->
<svg class="footer-wave" viewBox="0 0 1200 726" preserveAspectRatio="none">
  <defs><linearGradient id="fg" x1="0" y1="0" x2="0" y2="1"><stop offset="0" stop-color="#44516a"/><stop offset="1" stop-color="#56647d"/></linearGradient></defs>
  <path d="M0 40 C120 70 160 190 330 200 C520 210 620 120 800 150 C960 175 1060 210 1200 200 L1200 726 L0 726Z" fill="url(#fg)"/>
  <path d="M0 330 C200 300 380 420 620 360 C820 310 1000 420 1200 380 L1200 330 C1000 370 820 250 620 320 C380 380 200 260 0 290Z" fill="#fff" opacity=".9"/>
</svg>

<section class="newsletter">
  <h3 class="nl-title">Subscribe Our Newsletter</h3>
  <p class="nl-text">Subscribe our newsletter to receive the latest news<br>and exclusive offers every week, No spam.</p>
  <div class="nl-field">
    <svg width="14" height="10"><rect x=".5" y=".5" width="13" height="9" fill="none" stroke="#8a93a2"/><path d="M.5 .5 7 6l6.5-5.5" fill="none" stroke="#8a93a2"/></svg>
    Enter email address
    <span class="nl-send"><svg width="16" height="16" viewBox="0 0 16 16"><path d="M15 1 1 7l5 2 2 5z" fill="#fff"/></svg></span>
  </div>
</section>

<div class="f-brand"><span class="brand-dot"></span>Veltrax</div>
<div class="socials"><span></span><span></span><span></span><span></span></div>
<a class="btn footer-btn">CONTACT US</a>

<div class="f-col" style="left:491px">
  <h4>Quick links</h4>
  <ul><li>Home</li><li>About Us</li><li>Services</li><li>Insights</li><li>Join Us</li><li>Contact Us</li></ul>
</div>
<div class="f-col" style="left:668px">
  <h4>Our Services</h4>
  <ul><li>Business Transformation</li><li>ERP Implementations</li><li>ERP Solutions</li><li>BI and Data</li><li>Building the Right Team...</li></ul>
</div>
<div class="f-col" style="left:898px">
  <h4>Contact info</h4>
  <div class="contact-item"><svg width="14" height="10"><rect width="14" height="10" fill="var(--gold)"/><path d="M0 0 7 6l7-6" fill="none" stroke="#4b5a73"/></svg>Email:<br>hello@veltrax.co</div>
  <div class="contact-item"><svg width="14" height="14" viewBox="0 0 14 14"><path d="M3 1 5 4 4 6c1 2 2 3 4 4l2-1 3 2-1 2C6 13 1 8 1 2z" fill="var(--gold)"/></svg>Phone:<br>+44 113 555 0142</div>
  <div class="contact-item"><svg width="12" height="15" viewBox="0 0 12 15"><path d="M6 0a6 6 0 0 0-6 6c0 4 6 9 6 9s6-5 6-9a6 6 0 0 0-6-6z" fill="var(--gold)"/><circle cx="6" cy="6" r="2" fill="#4b5a73"/></svg>Location:<br>Some address line goes here city name</div>
</div>

<div class="copyright">© Veltrax Design 2023, All Rights Reserved</div>
<div class="chat"><svg width="22" height="20" viewBox="0 0 22 20"><path d="M11 1C5 1 1 4.5 1 9c0 2.5 1.3 4.6 3.3 6L3 19l4.6-2.4c1 .3 2.2.4 3.4.4 6 0 10-3.5 10-8s-4-8-10-8z" fill="#fff"/></svg></div>

</body>
</html>
```